Prairie Lantern Jubilee

Organization:
Prairie Lantern Jubilee is a non-profit organization created by a group of anonymous donors to bring more fun, culture, and art to a small Texas town. Our mission is to promote art and music in Caldwell Ridge County.
The multi-day eclectic festival will feature three stages, a film, art vendors, live mural artists, and food trucks set up throughout historic downtown Oakvale. The event is FREE to the public.
Goals:
We need an attractive poster to publicize the festival.
Details:
Prairie Lantern Jubilee
Friday, October 14 – 16
Free admission (VIP tickets available)
Live music- 3 stages/10 bands
Film Screening
Art vendors and art walk
Live art murals
Food trucks
www.prairielanternjubilee.example
#prairielantern
Requirements:
Please incorporate our festival logo attached.
Conclusion:
After selecting a poster design, we hope to continue to work with the artist to design other event materials including website splash page and rack cards using design elements from the poster.

```html
<!DOCTYPE html>
<html lang="en">
<head>
<meta charset="utf-8">
<title>Prairie Lantern Jubilee</title>
<link href="https://fonts.googleapis.com/css2?family=Oswald:wght@400;500;700&family=Roboto+Condensed:wght@400;700&family=Black+Ops+One&family=Archivo+Black&display=swap" rel="stylesheet">
<style>
  :root {
    --night: #0b0b0b;
    --ink: #1d1d1d;
    --white: #ffffff;
    --orange: #f7941d;
  }
  html, body { margin: 0; padding: 0; overflow: hidden; background: var(--night); }
  .poster {
    position: relative; width: 776px; height: 1200px; overflow: hidden;
    background: var(--night); font-family: "Oswald", sans-serif;
  }
  .paper { position: absolute; inset: 0; }
  .layer { position: absolute; left: 0; right: 0; text-align: center; margin: 0; padding: 0; }
  .date-line {
    top: 96px; font-family: "Archivo Black", sans-serif; font-size: 19px;
    color: var(--white); letter-spacing: 0.5px; text-shadow: 0 2px 3px rgba(0,0,0,.55);
  }
  .festival-mark {
    top: 238px; display: flex; justify-content: center; align-items: center; gap: 16px;
  }
  .festival-mark .dot { width: 34px; height: 34px; border-radius: 50%; background: var(--ink); }
  .festival-mark .name {
    font-family: "Oswald", sans-serif; font-weight: 700; font-size: 52px;
    color: var(--ink); text-transform: uppercase; letter-spacing: 1px;
  }
  .features {
    top: 480px; font-family: "Archivo Black", sans-serif; font-size: 16px; line-height: 30px;
    color: var(--white); text-transform: uppercase; text-shadow: 0 2px 3px rgba(0,0,0,.7);
  }
  .admission {
    top: 548px; font-family: "Black Ops One", sans-serif; font-size: 31px; line-height: 38px;
    color: var(--orange); letter-spacing: 1px; text-shadow: 0 2px 2px rgba(0,0,0,.35);
  }
  .admission small {
    display: block; font-family: "Archivo Black", sans-serif; font-size: 14px; line-height: 18px; letter-spacing: 0.5px;
  }
  .schedule {
    top: 619px; font-family: "Roboto Condensed", sans-serif; font-size: 14.5px; line-height: 15.6px;
    color: var(--ink); text-transform: uppercase; letter-spacing: 0.9px; list-style: none;
  }
  .schedule .day { font-weight: 700; text-decoration: underline; }
  .sponsors {
    top: 1032px; display: flex; justify-content: center; align-items: center; gap: 18px;
    white-space: nowrap;
  }
  .sponsor {
    display: flex; align-items: center; gap: 6px; font-family: "Oswald", sans-serif;
    font-size: 12px; font-weight: 500; color: var(--ink); text-transform: uppercase;
  }
  .sponsor .mark { width: 24px; height: 24px; border-radius: 50%; background: var(--ink); }
  .badge { width: 36px; height: 36px; border-radius: 50%; background: var(--ink); flex: none; }
  .badge.square { border-radius: 3px; width: 40px; height: 32px; }
  .sponsor.boxed { background: var(--ink); color: var(--white); padding: 8px 12px; }
  .web {
    top: 1086px; font-family: "Archivo Black", sans-serif; font-size: 22px; color: var(--white);
    text-shadow: 0 2px 3px rgba(0,0,0,.6);
  }
  .tag {
    top: 1118px; font-family: "Archivo Black", sans-serif; font-size: 22px; color: var(--white);
    text-shadow: 0 2px 3px rgba(0,0,0,.6); text-transform: uppercase;
  }
</style>
</head>
<body>
<div class="poster">
  <svg class="paper" width="776" height="1200" viewBox="0 0 776 1200" aria-hidden="true">
    <defs>
      <linearGradient id="paperBase" x1="0" y1="0" x2="0.3" y2="1">
        <stop offset="0" stop-color="#5f8088"/>
        <stop offset="0.22" stop-color="#7b8e9a"/>
        <stop offset="0.5" stop-color="#d8c27a"/>
        <stop offset="0.68" stop-color="#e7cf7e"/>
        <stop offset="0.85" stop-color="#cfa960"/>
        <stop offset="1" stop-color="#8fa46a"/>
      </linearGradient>
      <radialGradient id="paperGlow" cx="0.55" cy="0.62" r="0.5">
        <stop offset="0" stop-color="#f4e4a2" stop-opacity="0.85"/>
        <stop offset="1" stop-color="#f4e4a2" stop-opacity="0"/>
      </radialGradient>
      <radialGradient id="paperShade" cx="0.5" cy="0.5" r="0.72">
        <stop offset="0.6" stop-color="#000" stop-opacity="0"/>
        <stop offset="1" stop-color="#1a1a10" stop-opacity="0.55"/>
      </radialGradient>
    </defs>
    <g>
      <polygon fill="url(#paperBase)" points="20,60 60,34 100,50 150,30 200,44 260,26 330,40 400,30 470,44 540,28 600,42 660,30 720,44 756,36 748,120 760,220 746,320 758,440 744,560 756,680 744,800 758,920 746,1020 756,1110 740,1168 680,1160 620,1172 540,1160 460,1174 380,1162 300,1174 220,1160 150,1172 80,1160 30,1170 34,1090 18,990 30,880 20,760 34,640 18,520 30,400 20,280 34,170"/>
      <polygon fill="url(#paperGlow)" points="20,60 60,34 100,50 150,30 200,44 260,26 330,40 400,30 470,44 540,28 600,42 660,30 720,44 756,36 748,120 760,220 746,320 758,440 744,560 756,680 744,800 758,920 746,1020 756,1110 740,1168 680,1160 620,1172 540,1160 460,1174 380,1162 300,1174 220,1160 150,1172 80,1160 30,1170 34,1090 18,990 30,880 20,760 34,640 18,520 30,400 20,280 34,170"/>
      <polygon fill="url(#paperShade)" points="20,60 60,34 100,50 150,30 200,44 260,26 330,40 400,30 470,44 540,28 600,42 660,30 720,44 756,36 748,120 760,220 746,320 758,440 744,560 756,680 744,800 758,920 746,1020 756,1110 740,1168 680,1160 620,1172 540,1160 460,1174 380,1162 300,1174 220,1160 150,1172 80,1160 30,1170 34,1090 18,990 30,880 20,760 34,640 18,520 30,400 20,280 34,170"/>
    </g>
  </svg>

  <div class="layer date-line">FRIDAY, OCTOBER 14 – 16, 2016</div>

  <div class="layer festival-mark">
    <span class="dot"></span>
    <span class="name">Prairie Lantern Jubilee</span>
  </div>

  <div class="layer features">
    Live Music- 3 Stages/10 Bands :: Film Screening<br>
    Art Vendors and Art Walk :: Live Art Murals :: Food Trucks
  </div>

  <div class="layer admission">
    FREE ADMISSION
    <small>( VIP TICKETS AVAILABLE )</small>
  </div>

  <ul class="layer schedule">
    <li class="day">Friday - Oct. 14th</li>
    <li>5:30 PM - Sponsor &amp; Artist Reception</li>
    <li>7 PM - Film Screening: Dust on the Fenceline</li>
    <li>8:30 PM - Music: To Be Announced @ Maple Row Farm Stage</li>
    <li class="day">Saturday - Oct. 15th</li>
    <li>Early Morning - Mural Artists Begin Their Work in Historic Downtown Oakvale</li>
    <li>11 AM - Art Village Opens @ Mill Street Inn</li>
    <li>11 AM - Food Truck Court Opens @ Maple Row Farm... Buy Your Own Food!</li>
    <li>12 PM - Music: Dana Whitlock @Maple Row Farm Stage</li>
    <li>1:00 PM - Music: Leo Marchetti @ Cedar Creek Brewing Stage</li>
    <li>2:00 PM - Music: Copper Hollow @Maple Row Farm Stage</li>
    <li>3 PM - Music: Wade Ellison @ Cedar Creek Brewing Stage</li>
    <li>3 PM - Prairie Pint Walk Begins Throughout Historic Downtown</li>
    <li>3 PM - Art Walk Begins Throughout Historic Downtown</li>
    <li>3:30 PM - VIP Tent Opens @ The Main Stage</li>
    <li>4 PM - Music: Nora Pruitt @ The Main Stage</li>
    <li>5:00 PM - Music: Cal Brandt @Maple Row Farm Stage</li>
    <li>6:30 PM - Music: Rails &amp; Rye @ The Main Stage</li>
    <li>7 PM - Prairie Pint Walk &amp; Art Walk Closed - Art Village &amp; Food Trucks Still Open</li>
    <li>8 PM - Art Village Closed.</li>
    <li>8:30 PM - Music: Lowdown Lanterns @ The Main Stage</li>
    <li class="day">Sunday - Oct. 16th</li>
    <li>Early Morning - Mural Artists Complete Their Work in Historic Downtown Oakvale</li>
    <li>11 AM - Art Village Opens @ Mill Street Inn</li>
    <li>12 PM - Music: The Velvet Tides @Maple Row Farm Stage</li>
    <li>3 PM - Art Village Closed</li>
  </ul>

  <div class="layer sponsors">
    <span class="sponsor"><span class="mark"></span>Maple Row Farm</span>
    <span class="sponsor">Side Door Gallery</span>
    <span class="badge"></span>
    <span class="sponsor">Cedar Creek Brewing</span>
    <span class="badge square"></span>
    <span class="sponsor boxed">Marisol Dressings</span>
    <span class="badge"></span>
    <span class="badge"></span>
  </div>

  <div class="layer web">WWW.PRAIRIELANTERNJUBILEE.EXAMPLE</div>
  <div class="layer tag">#prairielantern</div>
</div>
</body>
</html>
```